Need Letterhead Design & Matching Business Card

I have a logo that I love already. But the letterhead is less than appealing and boring. I'd like a design for my letterhead which I will match with business cards. Also, I'd like to have used fonts that are generally available, as my current letterhead uses a font named "SPACE" which nobody has unless they download it...so when a Word version is forwarded, it looks awful on the receiver's screed due to not having the font. That being said, modern is the look we like and are going for.

My business is "Halloran Brightmoor PC" - a law firm specializing in representing people who have suffered catastrophic injuries or death (plane, auto, train crashes etc.).

See attached letterhead, which has all of the pertinent information. My logo is also attached in various formats.

```html
<!DOCTYPE html>
<html lang="en">
<head>
<meta charset="utf-8">
<title>Halloran Brightmoor PC — Letterhead</title>
<link href="https://fonts.googleapis.com/css2?family=Montserrat:wght@300;400&display=swap" rel="stylesheet">
<style>
  :root {
    --canvas-bg: #f2f2f4;
    --paper: #ffffff;
    --band: #0c0c0c;
    --band-pattern: #1b1b1b;
    --mark-text: #f2f2f2;
    --footer-text: #9a9a9a;
    --footer-strong: #cfcfcf;
  }
  * { box-sizing: border-box; margin: 0; padding: 0; }
  html, body {
    width: 686px;
    height: 1200px;
    overflow: hidden;
    background: var(--canvas-bg);
    font-family: "Montserrat", Arial, sans-serif;
  }
  .letterhead {
    position: absolute;
    left: 63px;
    top: 237px;
    width: 560px;
    height: 725px;
    background: var(--paper);
    display: flex;
    flex-direction: column;
    justify-content: space-between;
  }
  .letterhead__header {
    height: 99px;
    background: var(--band);
    display: flex;
    align-items: center;
    justify-content: center;
  }
  .firm-name {
    color: var(--mark-text);
    font-weight: 300;
    font-size: 25px;
    letter-spacing: 3px;
    text-transform: uppercase;
    white-space: nowrap;
  }
  .letterhead__footer {
    height: 49px;
    background: var(--band);
    display: flex;
    justify-content: space-between;
    align-items: center;
    padding: 0 67px 0 67px;
    font-size: 5.6px;
    letter-spacing: 1.1px;
    text-transform: uppercase;
    color: var(--footer-text);
    line-height: 12.5px;
  }
  .contact--right { text-align: right; }
  .contact__sep { color: var(--footer-strong); padding: 0 3px; }
  .contact__phone {
    color: var(--footer-strong);
    font-size: 7.2px;
    letter-spacing: 1.4px;
  }
</style>
</head>
<body>
  <main class="letterhead">
    <header class="letterhead__header">
      <h1 class="firm-name">Halloran Brightmoor PC</h1>
    </header>
    <footer class="letterhead__footer">
      <address class="contact contact--left" style="font-style:normal">
        <div>R. Daniel Okafor, Esq.<span class="contact__sep">|</span>President</div>
        <div>4410 Meridian Ave.<span class="contact__sep">|</span>Suite 800</div>
        <div>Los Angeles, CA 90024</div>
      </address>
      <address class="contact contact--right" style="font-style:normal">
        <div>daniel@halloranbrightmoor.com</div>
        <div>www.halloranbrightmoor.com</div>
        <div class="contact__phone">Tel: (855) 555-0147</div>
      </address>
    </footer>
  </main>
</body>
</html>
```